Cyber security company needs a flyer to promote its anti email phishing product

We need a flyer design for a new company based out of Cheltenham, England called 'Vaultmark'. We develop software that stops employees opening phishing emails. Our initial product is called 'Halcyon' - designed as a innovative new way to prevent phishing emails tricking employees from opening them. The solution is designed for Enterprise customers so it must have a corporate feel. Vaultmark is part of the latest BRTX accelerator so we are allowed to also use the BRTX and PLMV (UK) logo. The final design should communicate innovation and security. I like the design 10290027 by Orwen as a general look and feel

Need to provide copy for flyer and 5 days on reflection is to short a time period hence extension 10 days .

Target Market(s)

Enterprise sized customers. No particular vertical is being targeted

Requirements
Must have
• Somewhere the BRTX and PLMV logos. The blue shield logo is the Vaultmark one. The .eps .ai format are higher quality but will need the vaultmark text removed.
• Looking for a single fold design so a A4 is effectively an A5 with 4 sides.
• www.vaultmarkholdings.example
• Tel no. 44 (0) 207 555 0371
• info@vaultmarkholdings.example
Nice to have
• Must have a quality and corporate feel

```html
<!DOCTYPE html>
<html lang="en">
<head>
<meta charset="utf-8">
<title>Vaultmark – Halcyon flyer</title>
<link rel="stylesheet" href="https://fonts.googleapis.com/css2?family=Montserrat:wght@400;600;700;800&family=Open+Sans:wght@400;600&display=swap">
<style>
  :root{
    --navy:#0c2a50;
    --navy-deep:#081d3a;
    --blue:#1c67b0;
    --cyan:#2aa6df;
    --ink:#3b4756;
    --muted:#7c8794;
    --paper:#ffffff;
    --canvas:#e8ebef;
    --rule:#d6dde5;
  }
  *{box-sizing:border-box;margin:0;padding:0}
  html,body{width:887px;height:1200px;overflow:hidden;background:var(--canvas)}
  body{position:relative;font-family:"Open Sans",Arial,sans-serif;color:var(--ink)}
  .spread{position:absolute;left:30px;width:828px;height:562px;display:flex;background:var(--paper);box-shadow:0 2px 6px rgba(0,0,0,.18)}
  .spread--outside{top:15px}
  .spread--inside{top:612px}
  .panel{position:relative;height:100%;overflow:hidden}
  .panel--a{width:266px}
  .panel--b{width:266px}
  .panel--c{width:296px}

  /* FAQ panel */
  .faq{background:linear-gradient(160deg,var(--navy) 0%,var(--navy-deep) 100%);color:#d7e3f1;padding:24px 20px}
  .faq__title{font-family:"Montserrat",sans-serif;font-weight:700;font-size:10px;letter-spacing:.08em;color:var(--cyan);margin-bottom:12px}
  .faq__q{font-family:"Montserrat",sans-serif;font-weight:700;font-size:7.6px;color:#fff;margin:9px 0 3px}
  .faq__a{font-size:6.8px;line-height:1.5;color:#b9c9dc}

  .photo{position:absolute;left:0;right:0}
  .photo--laptop{top:0;height:265px;background:linear-gradient(135deg,#0d3566 0%,#1f6cb4 55%,#6fb6e6 100%)}
  .photo--lock{top:130px;height:245px;background:radial-gradient(circle at 55% 45%,#6cc3ee 0%,#1f6fb8 45%,#0b2d58 100%)}
  .photo--screen{top:0;height:200px;background:linear-gradient(120deg,#15406f 0%,#3b86c6 50%,#a9d2ee 100%)}
  .photo--worker{top:372px;height:190px;background:linear-gradient(160deg,#1a5795 0%,#0c2a50 100%)}

  /* contact panel */
  .contact{position:absolute;left:22px;top:292px;list-style:none}
  .contact__item{display:flex;align-items:center;gap:9px;font-size:8px;color:var(--ink);margin-bottom:9px}
  .contact__icon{width:16px;height:16px;border-radius:50%;background:var(--blue);display:flex;align-items:center;justify-content:center}
  .brand{position:absolute;display:flex;align-items:center;gap:7px}
  .brand__mark{width:26px;height:26px;background:var(--blue)}
  .brand__name{font-family:"Montserrat",sans-serif;font-weight:700;font-size:14px;color:var(--navy)}
  .brand--back{left:22px;top:470px}
  .back-note{position:absolute;left:140px;top:440px;width:110px;font-size:6.6px;line-height:1.5;color:var(--muted)}

  /* cover */
  .cover__headline{position:absolute;left:22px;top:22px;width:260px;font-family:"Montserrat",sans-serif;font-weight:800;font-size:19px;line-height:1.2;color:var(--navy)}
  .accent{color:var(--cyan)}
  .brand--cover{left:22px;top:400px}
  .cover__note{position:absolute;left:150px;top:396px;width:128px;font-size:6.6px;line-height:1.5;color:var(--muted)}
  .cover__bar{position:absolute;left:0;right:0;bottom:0;height:40px;background:var(--blue);display:flex;align-items:center;justify-content:flex-end;padding-right:18px}
  .cover__url{font-family:"Montserrat",sans-serif;font-weight:700;font-size:9px;color:#fff;letter-spacing:.03em}

  /* inside */
  .intro{padding:24px 20px 0}
  .intro__headline{font-family:"Montserrat",sans-serif;font-weight:800;font-size:15px;line-height:1.25;color:var(--navy);margin-bottom:12px}
  .body-copy{font-size:7px;line-height:1.6;color:var(--ink);margin-bottom:8px}

  .feature{position:absolute;width:118px}
  .feature__icon{width:40px;height:40px;border-radius:50%;border:2px solid var(--cyan);display:flex;align-items:center;justify-content:center;margin-bottom:6px}
  .feature__title{font-family:"Montserrat",sans-serif;font-weight:700;font-size:7.6px;color:var(--navy);margin-bottom:4px}
  .feature__text{font-size:6.5px;line-height:1.5;color:var(--muted)}
  .feature--detect{left:18px;top:216px}
  .feature--react{left:140px;top:216px}
  .feature--smart{left:18px;top:340px}
  .feature--alert{left:22px;top:248px;width:250px}

  .benefits{position:absolute;left:0;top:0;right:0;height:232px;background:linear-gradient(160deg,var(--navy) 0%,var(--navy-deep) 100%);padding:24px 22px;color:#c7d6e8}
  .benefits__title{font-family:"Montserrat",sans-serif;font-weight:800;font-size:13px;color:#fff;margin-bottom:10px}
  .benefits .body-copy{color:#c7d6e8}

  .protect{position:absolute;left:266px;right:0;top:462px;height:52px;background:var(--navy);padding:9px 20px;color:#c7d6e8}
  .protect__title{font-family:"Montserrat",sans-serif;font-weight:700;font-size:9px;color:#fff;margin-bottom:4px;letter-spacing:.04em}
  .protect__text{font-size:6.4px;line-height:1.5}
  .partners{position:absolute;left:266px;right:0;top:514px;height:48px;display:flex;align-items:center;justify-content:flex-end;gap:16px;padding-right:20px}
  .partner-badge{height:24px;background:#c9d2dc}
  .partner-badge--a{width:52px}
  .partner-badge--b{width:30px;border-radius:50%}
  .partner-badge--c{width:74px}
</style>
</head>
<body>

<section class="spread spread--outside">
  <div class="panel panel--a faq">
    <h3 class="faq__title">FREQUENTLY ASKED QUESTIONS</h3>
    <p class="faq__q">Why should I consider Vaultmark's Halcyon solution?</p>
    <p class="faq__a">Halcyon stops targeted phishing before staff can open it, learning from live threats and adapting to new attacks across your whole organisation.</p>
    <p class="faq__q">Does Halcyon replace any of my existing tools?</p>
    <p class="faq__a">No, it works alongside your current email and security stack.</p>
    <p class="faq__q">What sort of business can benefit from Halcyon?</p>
    <p class="faq__a">Any enterprise with large volumes of inbound email and staff who handle sensitive data, finances or customer records can benefit immediately.</p>
    <p class="faq__q">What about data analytics?</p>
    <p class="faq__a">Clear dashboards show attempted attacks, response times and trends so your security team can report risk and act with confidence.</p>
    <p class="faq__q">How does Halcyon training and phishing work?</p>
    <p class="faq__a">Short, realistic exercises keep staff alert and measure progress over time.</p>
  </div>

  <div class="panel panel--b">
    <div class="photo photo--laptop" role="img" aria-label="Photo of hands typing on a laptop with glowing security graphics"></div>
    <ul class="contact">
      <li class="contact__item"><span class="contact__icon"><svg width="9" height="9" viewBox="0 0 24 24" fill="#fff"><path d="M6.6 10.8a15.1 15.1 0 006.6 6.6l2.2-2.2a1 1 0 011-.25 11.4 11.4 0 003.6.6 1 1 0 011 1V20a1 1 0 01-1 1A17 17 0 013 4a1 1 0 011-1h3.5a1 1 0 011 1 11.4 11.4 0 00.6 3.6 1 1 0 01-.25 1z"/></svg></span>44 (0) 207 555 0371</li>
      <li class="contact__item"><span class="contact__icon"><svg width="9" height="9" viewBox="0 0 24 24" fill="none" stroke="#fff" stroke-width="2.4"><rect x="3" y="5" width="18" height="14"/><path d="M3 6l9 7 9-7"/></svg></span>info@vaultmarkholdings.example</li>
      <li class="contact__item"><span class="contact__icon"><svg width="9" height="9" viewBox="0 0 24 24" fill="none" stroke="#fff" stroke-width="2.2"><circle cx="12" cy="12" r="9"/><path d="M3 12h18M12 3c3 3 3 15 0 18M12 3c-3 3-3 15 0 18"/></svg></span>www.vaultmarkholdings.example</li>
    </ul>
    <p class="back-note">Vaultmark helps enterprises defend staff and networks from targeted email attacks.</p>
    <div class="brand brand--back"><span class="brand__mark"></span><span class="brand__name">vaultmark</span></div>
  </div>

  <div class="panel panel--c">
    <h1 class="cover__headline">NEED TO <span class="accent">PROTECT</span> YOUR DATA AND NETWORKS FROM TARGETED EMAIL PHISHING?</h1>
    <div class="photo photo--lock" role="img" aria-label="Photo of a hand touching a glowing digital padlock"></div>
    <div class="brand brand--cover"><span class="brand__mark"></span><span class="brand__name">vaultmark</span></div>
    <p class="cover__note">Halcyon detects spear phishing and alerts staff before damage is done.</p>
    <div class="cover__bar"><span class="cover__url">www.vaultmarkholdings.example</span></div>
  </div>
</section>

<section class="spread spread--inside">
  <div class="panel panel--a">
    <div class="intro">
      <h2 class="intro__headline">HALCYON IS A NEW APPROACH TO <span class="accent">DETECTING SPEAR PHISHING</span></h2>
      <p class="body-copy">Vaultmark's product, called Halcyon, is a smarter way of stopping phishing emails that trick employees. Built for enterprise teams, it checks every message in real time and flags the ones designed to deceive.</p>
      <p class="body-copy">At Vaultmark we believe people are the last line of defence, so Halcyon gives them clear warnings at the moment they need them, without slowing down everyday work.</p>
    </div>
    <div class="photo photo--worker" role="img" aria-label="Photo of a professional working at a laptop"></div>
  </div>

  <div class="panel panel--b">
    <div class="photo photo--screen" role="img" aria-label="Photo of a businessman touching a digital interface"></div>
    <div class="feature feature--detect">
      <div class="feature__icon"><svg width="20" height="20" viewBox="0 0 24 24" fill="none" stroke="#1c67b0" stroke-width="2"><rect x="3" y="5" width="18" height="14"/><path d="M3 6l9 7 9-7"/></svg></div>
      <p class="feature__title">DETECT PHISHING EMAILS</p>
      <p class="feature__text">Every inbound message is scanned for signs of targeted deception.</p>
    </div>
    <div class="feature feature--react">
      <div class="feature__icon"><svg width="20" height="20" viewBox="0 0 24 24" fill="#1c67b0"><path d="M13 2L4 14h7l-1 8 9-12h-7z"/></svg></div>
      <p class="feature__title">REACT</p>
      <p class="feature__text">Suspicious mail is held and your team is told instantly.</p>
    </div>
    <div class="feature feature--smart">
      <div class="feature__icon"><svg width="20" height="20" viewBox="0 0 24 24" fill="none" stroke="#1c67b0" stroke-width="2"><path d="M9 18h6M10 21h4M12 3a6 6 0 00-4 10.5c.7.7 1 1.5 1 2.5h6c0-1 .3-1.8 1-2.5A6 6 0 0012 3z"/></svg></div>
      <p class="feature__title">SMART</p>
      <p class="feature__text">Halcyon learns from each attack and keeps improving its detection.</p>
    </div>
  </div>

  <div class="panel panel--c">
    <div class="benefits">
      <h3 class="benefits__title">BENEFITS</h3>
      <p class="body-copy">Halcyon reduces the risk of costly breaches by stopping deceptive emails before staff act on them, protecting data and reputation.</p>
      <p class="body-copy">It fits alongside existing email systems, needs little setup and gives security teams clear reporting across the organisation.</p>
      <p class="body-copy">Staff gain confidence as simple prompts help them spot threats on their own.</p>
    </div>
    <div class="feature feature--alert">
      <div class="feature__icon"><svg width="20" height="20" viewBox="0 0 24 24" fill="none" stroke="#1c67b0" stroke-width="2"><path d="M18 16V11a6 6 0 00-12 0v5l-2 2h16zM10 21h4"/></svg></div>
      <p class="feature__title">ALERT</p>
      <p class="feature__text">Clear warnings appear at the moment of risk, so employees know when to pause and report.</p>
    </div>
  </div>

  <div class="protect">
    <p class="protect__title">PROTECTING YOUR ORGANISATION</p>
    <p class="protect__text">Vaultmark is part of the BRTX accelerator and works with PLMV guidance to keep enterprise teams safe from phishing.</p>
  </div>
  <div class="partners">
    <span class="partner-badge partner-badge--a"></span>
    <span class="partner-badge partner-badge--b"></span>
    <span class="partner-badge partner-badge--c"></span>
  </div>
</section>

</body>
</html>
```